Coral Bay Villa Offer

I need a flyer that i can use at different venues that offers the same thing - a complimentary stay in the Linden Feast company owned Coral Bay Villa for 4 nights and 5 days. I need a template of a design that i can modify so it's venue specific. For example, i want it to say: "Confirm your reservation at XXXXXXX venue alongside the Linden Feast and receive a complimentary stay in the Linden Feast's company owned villa for 4 nights and 5 days! Daily cleaning, shopping and cooking is included."

Target Market(s)

Wedding Clients for our catering company at different off site wedding venues.

Industry/Entity Type

Wedding

Font styles to use
Serif

Colors

Designer to choose colors to be used in the design.

Requirements
Must have
• Linden Feast Logo
• Stylized Photos of the condo and puerto vallarta in general
Nice to have
• The Linden Feast is the Highest Rated Caterer in California on RAVO
• The Linden Feast offers turn key discounted all inclusive wedding vendor packages

```html
<!DOCTYPE html>
<html lang="en">
<head>
<meta charset="utf-8">
<title>Vive Vallarta – The Linden Feast</title>
<link rel="stylesheet" href="https://fonts.googleapis.com/css2?family=Playfair+Display:wght@400;700;900&family=Source+Sans+3:ital,wght@0,400;1,400&display=swap">
<style>
  :root {
    --paper: #ffffff;
    --ink: #231f20;
    --text: #2b2b2b;
    --mark: #262223;
  }
  * { margin: 0; padding: 0; box-sizing: border-box; }
  html, body { width: 925px; height: 1200px; overflow: hidden; background: var(--paper); }
  .flyer {
    position: relative;
    width: 925px;
    height: 1200px;
    background: var(--paper);
    color: var(--text);
    font-family: "Source Sans 3", "Myriad Pro", sans-serif;
  }
  .headline {
    position: absolute;
    top: 14px; left: 0; width: 100%;
    text-align: center;
    font-family: "Playfair Display", "Bodoni Moda", serif;
    font-weight: 900;
    font-size: 78px;
    letter-spacing: -1px;
    color: var(--ink);
    line-height: 1;
  }
  .subhead {
    position: absolute;
    top: 102px; left: 0; width: 100%;
    text-align: center;
    font-family: "Playfair Display", serif;
    font-weight: 700;
    font-size: 29px;
    letter-spacing: -0.5px;
    color: var(--ink);
  }
  .offer {
    position: absolute;
    top: 170px; left: 0; width: 100%;
    text-align: center;
    font-size: 27.5px;
    line-height: 35px;
    color: var(--text);
  }
  .offer .included {
    display: block;
    margin-top: 2px;
    font-style: italic;
    font-size: 24px;
  }
  .photo {
    position: absolute;
  }
  .photo--resort {
    left: 71px; top: 345px; width: 481px; height: 291px;
    background: linear-gradient(180deg, #4f8fd6 0%, #9cc2e4 22%, #e9ebe6 42%, #6f8a4a 70%, #2d8ec9 88%, #3c6a3a 100%);
  }
  .photo--lounge {
    left: 564px; top: 345px; width: 290px; height: 360px;
    background: linear-gradient(180deg, #bdb7a8 0%, #8f8a78 30%, #2a2624 55%, #1a1716 75%, #4b4638 100%);
  }
  .photo--terrace {
    left: 71px; top: 649px; width: 484px; height: 293px;
    background: linear-gradient(180deg, #b9b8b4 0%, #8c8b88 28%, #4b4a3e 45%, #3a2a28 70%, #2a2524 100%);
  }
  .photo--living {
    left: 567px; top: 716px; width: 288px; height: 225px;
    background: linear-gradient(160deg, #d9d6cf 0%, #c9c3b8 30%, #9a3a2e 48%, #6a4c40 70%, #c9b7a2 100%);
  }
  .credentials {
    position: absolute;
    top: 975px; left: 0; width: 100%;
    text-align: center;
    font-size: 20px;
    line-height: 31px;
    color: var(--text);
  }
  .brand {
    position: absolute;
    top: 1091px; left: 305px;
    display: flex;
    align-items: flex-start;
    gap: 12px;
  }
  .brand__square {
    width: 85px; height: 77px;
    background: var(--mark);
  }
  .brand__name {
    font-family: "Playfair Display", serif;
    font-weight: 400;
    color: var(--mark);
    line-height: 1;
  }
  .brand__title {
    display: block;
    font-size: 31px;
    letter-spacing: 1px;
    margin-top: 1px;
  }
  .brand__line {
    display: block;
    font-size: 12px;
    letter-spacing: 9.4px;
    margin-top: 8px;
  }
  .brand__line + .brand__line { margin-top: 5px; }
</style>
</head>
<body>
  <main class="flyer">
    <h1 class="headline">VIVE VALLARTA</h1>
    <p class="subhead">with the Linden Feast</p>

    <p class="offer">
      Confirm your reservation at the XXXXXXX<br>
      along with the Linden Feast and receive a complimentary<br>
      stay in the company owned villa for 4 nights and 5 days.
      <span class="included">Daily cleaning, shopping and cooking is included.</span>
    </p>

    <div class="photo photo--resort" role="img" aria-label="Hillside white villa complex with terraced balconies, palm trees and a curved blue pool with sun loungers"></div>
    <div class="photo photo--lounge" role="img" aria-label="Villa living room with dark sectional sofa, red glass chandelier and open glass doors to the terrace"></div>
    <div class="photo photo--terrace" role="img" aria-label="Covered terrace with red cushioned seating and dining table overlooking the bay at dusk"></div>
    <div class="photo photo--living" role="img" aria-label="Bright open-plan lounge with leather sofa, red accent wall, red vase and dining area"></div>

    <p class="credentials">
      The Linden Feast offers turn key discounted all inclusive wedding vendor packages<br>
      The Linden Feast is the Highest Rated Caterer in California on RAVO
    </p>

    <div class="brand">
      <div class="brand__square"></div>
      <div class="brand__name">
        <span class="brand__title">THE LINDEN FEAST</span>
        <span class="brand__line">CATERING &amp;</span>
        <span class="brand__line">EVENT DESIGN</span>
      </div>
    </div>
  </main>
</body>
</html>
```